Tea Shop - Drinks Menu - Vertical TV screen

Need a drinks menu design for a tea shop based in The Netherlands. Called BrewHaven.
Currently we are trying to attract more customers for our SipAway and the idea came up to place 3 TV screen vertically in order to use 2 for the menu.
Website: http://brewhaven-velden.example.nl/
Posible colour themes -
- Light green (same green as logo)
- Light brown
Dimensions of the screen -
- 40inch
- 905 mm Height
- 207 mm Width
Resolution of the menu must be 1920x1080 BUT VERTICAL
Needs to contain the following -
- Hot SipAway
- BLACK
- Delicate Earl Grey
- Golden Sun Kiss
- Rosy Orchard
- Spicy Chai
- Black Assam
- Duchess of Hills
- Smokey Lapsang Suochong
- ( and many more teas, so leave space for aditional 5+)
- GREEN
- Sencha Lime-Ginger
- Sencha Forest Berries
- Sencha Orange Choco
- Happy Blossom
- Bancha
- Classic Gunpowder
- (space for aditional 4+)
- OOLONG
- Bullet Oolong
- Milky Oolong
- WHITE
- Bai Mu Tan
- HERBAL
- BrewHaven's Cloud
- Revitalising Kamille
- Pure Ginger
- Moon Blend
- Nana Mint
- Basil Strawberry
- FRUIT TEA
- Fruity Almond
- Berry Jolly
- Papaya Hug
- Spicy Pear
- Turkish Apple
- (space for aditional 2+)
- LATTÉ
- Spiced Chai
- Green Chai
- Vanille Chai
- Matcha
- Fresh Mint tea
- Iced Tea
- Peach
- Raspberry
- Lemon
- Mango
Divide this menu over 2 TV screens with the mentioned dimensions and use the font provided in the uploaded files (not mandatory if you think you have a bette idea).
Simple
Needs to attract people
Easy to adjust
Idea's are always welcome and appreciated
LOGO LINK : http://img.pictobox.example/7kq4zr9.png
(image too big to upload on here, sorry)
Target Market(s)
people whom drink TEA
Industry/Entity Type
Tv

```html
<!DOCTYPE html>
<html lang="en">
<head>
<meta charset="utf-8">
<title>BrewHaven – Drinks Menu Screens</title>
<link href="https://fonts.googleapis.com/css2?family=PT+Sans:wght@400;700&display=swap" rel="stylesheet">
<style>
  :root {
    --stage: #efe6d6;
    --ink: #3b2a22;
    --brand-green: #9cc93b;
    --white: #ffffff;
    --amber-base: #e9d784;
    --amber-wash: #c9bf4c;
    --lime-base: #d4ea8b;
    --lime-wash: #8fd04c;
    --cup-light: #ecdcc0;
    --cup-dark: #b48a5e;
    --leaf: #7bb04a;
  }
  * { box-sizing: border-box; margin: 0; padding: 0; }
  html, body { width: 699px; height: 1200px; overflow: hidden; }
  body {
    background: var(--stage);
    font-family: "PT Sans", "Myriad Pro", sans-serif;
    color: var(--ink);
    position: relative;
  }
  .screen {
    position: absolute;
    top: 18px;
    width: 267px;
    height: 1164px;
    overflow: hidden;
    box-shadow: 4px 5px 6px rgba(0,0,0,.18);
  }
  .screen--left { left: 39px; background: var(--amber-base); }
  .screen--right { left: 377px; background: var(--lime-base); }
  .screen__wash {
    position: absolute; left: 0; top: 100px; width: 100%; height: 380px;
  }
  .screen--left .screen__wash { background: radial-gradient(ellipse at 50% 25%, var(--amber-wash) 0%, rgba(233,215,132,0) 70%); }
  .screen--right .screen__wash { background: radial-gradient(ellipse at 50% 25%, var(--lime-wash) 0%, rgba(212,234,139,0) 70%); }
  .screen__crest { position: absolute; left: 0; top: 0; width: 267px; height: 180px; }
  .brand {
    position: absolute; top: 40px; left: 0; width: 100%;
    text-align: center;
    font-size: 36px; font-weight: 400; color: var(--brand-green);
    line-height: 1;
  }
  .photo {
    position: absolute; left: 0; bottom: 0; width: 100%;
  }
  .screen--left .photo { height: 318px; background: linear-gradient(180deg, rgba(236,220,192,0) 0%, var(--cup-light) 18%, var(--cup-dark) 62%, var(--cup-light) 100%); }
  .screen--right .photo { height: 304px; background: linear-gradient(180deg, rgba(236,220,192,0) 0%, #e4ecd0 18%, #cfe29a 40%, var(--cup-dark) 75%, var(--cup-light) 100%); }
  .menu-section { position: absolute; left: 0; width: 100%; text-align: center; }
  .menu-section__title { font-size: 21px; font-weight: 400; line-height: 26px; }
  .menu-section__list { list-style: none; margin-top: 4px; }
  .menu-section__list li { font-size: 18px; line-height: 29px; white-space: nowrap; }
  .menu-section__list li::before { content: "• "; font-size: 12px; }
  .divider {
    position: absolute; left: 50%; width: 12px; height: 12px; margin-left: -6px;
    border-radius: 50%; background: var(--leaf); opacity: .8;
  }
</style>
</head>
<body>

<section class="screen screen--left">
  <div class="screen__wash"></div>
  <svg class="screen__crest" viewBox="0 0 267 180" aria-hidden="true">
    <rect x="0" y="0" width="267" height="80" fill="#ffffff"/>
    <ellipse cx="133" cy="40" rx="150" ry="134" fill="#ffffff"/>
  </svg>
  <div class="brand">BrewHaven</div>
  <div class="photo" role="img" aria-label="Photo of an iced tea in a cup with a pink straw and brand sleeve"></div>

  <div class="menu-section" style="top:200px">
    <h2 class="menu-section__title">Hot SipAway</h2>
    <ul class="menu-section__list">
      <li>BLACK</li><li>Delicate Earl Grey</li><li>Golden Sun Kiss</li><li>Rosy Orchard</li>
      <li>Spicy Chai</li><li>Black Assam</li><li>Duchess of Hills</li><li>Smokey Lapsang Suochong</li>
    </ul>
  </div>
  <span class="divider" style="top:478px" role="img" aria-label="Leaf ornament"></span>

  <div class="menu-section" style="top:511px">
    <h2 class="menu-section__title">GREEN</h2>
    <ul class="menu-section__list">
      <li>Sencha Lime-Ginger</li><li>Sencha Forest Berries</li><li>Sencha Orange Choco</li>
      <li>Happy Blossom</li><li>Bancha</li><li>Classic Gunpowder</li>
    </ul>
  </div>
  <span class="divider" style="top:720px" role="img" aria-label="Leaf ornament"></span>

  <div class="menu-section" style="top:763px">
    <h2 class="menu-section__title">OOLONG</h2>
    <ul class="menu-section__list">
      <li>Bullet Oolong</li><li>Milky Oolong</li>
    </ul>
  </div>
  <span class="divider" style="top:852px" role="img" aria-label="Leaf ornament"></span>

  <div class="menu-section" style="top:898px">
    <h2 class="menu-section__title">WHITE</h2>
    <ul class="menu-section__list">
      <li>Bai Mu Tan</li>
    </ul>
  </div>
</section>

<section class="screen screen--right">
  <div class="screen__wash"></div>
  <svg class="screen__crest" viewBox="0 0 267 180" aria-hidden="true">
    <rect x="0" y="0" width="267" height="80" fill="#ffffff"/>
    <ellipse cx="133" cy="40" rx="150" ry="134" fill="#ffffff"/>
  </svg>
  <div class="brand">BrewHaven</div>
  <div class="photo" role="img" aria-label="Photo of a matcha latte in a cup with brand sleeve and a tea tin"></div>

  <div class="menu-section" style="top:200px">
    <h2 class="menu-section__title">HERBAL</h2>
    <ul class="menu-section__list">
      <li>BrewHaven's Cloud</li><li>Revitalising Kamille</li><li>Pure Ginger</li>
      <li>Moon Blend</li><li>Nana Mint</li><li>Basil Strawberry</li>
    </ul>
  </div>
  <span class="divider" style="top:413px" role="img" aria-label="Leaf ornament"></span>

  <div class="menu-section" style="top:441px">
    <h2 class="menu-section__title">FRUIT TEA</h2>
    <ul class="menu-section__list">
      <li>Fruity Almond</li><li>Berry Jolly</li><li>Papaya Hug</li><li>Spicy Pear</li><li>Turkish Apple</li>
    </ul>
  </div>
  <span class="divider" style="top:629px" role="img" aria-label="Leaf ornament"></span>

  <div class="menu-section" style="top:656px">
    <h2 class="menu-section__title">LATTÉ</h2>
    <ul class="menu-section__list">
      <li>Spiced Chai</li><li>Green Chai</li><li>Vanille Chai</li><li>Matcha</li>
    </ul>
  </div>
  <span class="divider" style="top:810px" role="img" aria-label="Leaf ornament"></span>

  <div class="menu-section" style="top:838px">
    <h2 class="menu-section__title">Fresh Mint tea</h2>
    <ul class="menu-section__list">
      <li>Iced Tea</li><li>Peach</li><li>Raspberry</li><li>Lemon</li><li>Mango</li>
    </ul>
  </div>
</section>

</body>
</html>
```